Bimvoro Power Point Presentation

We need our presentation designed. Our current presentation is inconsistent, too text heavy, and complicated. We want this to be clean, sleek, and impressive as our references attached are.

Our colors are blue, black, and white.
Our font is roboto.

```html
<!DOCTYPE html>
<html lang="en">
<head>
<meta charset="utf-8">
<title>Bimvoro Media Kit 2021</title>
<link href="https://fonts.googleapis.com/css2?family=Roboto:wght@300;400;500;700&display=swap" rel="stylesheet">
<style>
:root{
  --blue:#0B8CF5;
  --blue-dark:#0870C8;
  --ink:#111111;
  --paper:#FFFFFF;
  --panel:#F4F5F7;
  --canvas:#E0E0E0;
  --muted:#555B63;
  --rule:#D5D8DD;
}
*{box-sizing:border-box;margin:0;padding:0}
html,body{width:698px;height:1200px;overflow:hidden;background:var(--canvas)}
body{font-family:'Roboto',Arial,sans-serif;color:var(--ink)}
.deck{width:698px;height:1200px;display:grid;grid-template-columns:323px 323px;grid-auto-rows:182px;column-gap:15px;row-gap:13px;padding:17px 18px}
.slide{position:relative;overflow:hidden;background:var(--paper)}
.slide--blue{background:var(--blue);color:var(--paper)}
.abs{position:absolute}

/* brand mark */
.brand{position:absolute;display:flex;align-items:center;gap:3px;font-weight:500}
.brand__box{display:block;background:currentColor;border-radius:2px}
.brand--cover{left:20px;top:20px;font-size:13px;color:var(--paper)}
.brand--cover .brand__box{width:11px;height:11px}
.brand--foot{right:7px;bottom:5px;font-size:4.5px;color:var(--blue)}
.brand--foot .brand__box{width:4px;height:4px;border-radius:1px}
.brand--foot-light{color:var(--paper)}

/* cover */
.cover__title{position:absolute;left:20px;top:69px;font-size:17px;line-height:21px;font-weight:300}
.cover__title b{font-weight:700}
.cover__btn{position:absolute;left:20px;top:140px;width:55px;height:12px;background:var(--ink);border-radius:2px;font-size:4.5px;font-weight:500;color:var(--paper);display:flex;align-items:center;justify-content:center}
.cover__mail{position:absolute;left:20px;top:158px;font-size:5px;font-weight:300}
.cover__photo{position:absolute;left:150px;top:0;width:173px;height:182px;border-top-left-radius:34px 91px;border-bottom-left-radius:34px 91px}
.cover__kit{position:absolute;right:8px;bottom:8px;background:rgba(40,40,40,.75);color:var(--paper);font-size:5px;font-weight:300;padding:2px 5px}
.photo--lobby{background:linear-gradient(135deg,#E4ECF1 0%,#B8C9D4 55%,#5E7282 100%)}
.photo--wall{background:linear-gradient(135deg,#2C3F5B 0%,#6C7F94 40%,#B59A6C 70%,#2B3A4A 100%)}
.photo--crowd{background:linear-gradient(135deg,#5B5F63 0%,#9FA4A8 50%,#3F4346 100%)}
.photo--salon{background:linear-gradient(160deg,#D9D3B9 0%,#C4BE9E 45%,#6E6A5A 100%)}
.photo--street{background:linear-gradient(160deg,#EDEEEE 0%,#C9CBCC 55%,#8A8D8F 100%)}

/* headings */
.heading{position:absolute;left:24px;top:21px;font-size:12px;line-height:14px;font-weight:300;color:var(--blue)}
.heading b{font-weight:700}
.lede{position:absolute;left:24px;top:38px;width:150px;font-size:4.3px;line-height:6px;font-weight:300;color:var(--muted)}
.panel{position:absolute;background:var(--panel)}
.notes{position:absolute;left:24px;bottom:8px;font-size:2.2px;line-height:3px;color:var(--muted)}

/* feature columns */
.cols{position:absolute;display:flex}
.col{flex:1;padding:0 4px;border-right:0.5px solid var(--rule)}
.col:last-child{border-right:none}
.col__head{font-size:5px;font-weight:500;text-align:center;margin-bottom:6px;line-height:6px}
.item{display:flex;align-items:center;gap:3px;margin-bottom:5px;font-size:3.6px;line-height:4.6px;color:var(--muted);font-weight:300}
.item--stack{flex-direction:column;text-align:center;gap:2px}
.icon{flex:none;width:14px;height:14px;border-radius:50%;background:var(--blue);display:flex;align-items:center;justify-content:center}
.icon svg{width:8px;height:8px}

/* statement */
.statement{position:absolute;left:24px;top:62px;width:240px;font-size:10.5px;line-height:13px;font-weight:300}
.statement b{font-weight:700}
.underline{position:absolute;left:24px;height:1.2px;background:var(--paper)}

/* network */
.bar{position:absolute;height:10px;background:var(--ink);color:var(--paper);font-size:4.8px;font-weight:300;padding-left:5px;display:flex;align-items:center}
.map{position:absolute;background:linear-gradient(135deg,#DDE3EA,#C5CDD7)}
.stat{position:absolute;text-align:right;color:var(--blue);font-weight:700;font-size:8px;line-height:8px}
.stat small{display:block;font-size:3.5px;line-height:4px;font-weight:300;color:var(--muted)}
.stat--left{text-align:left}
.venue-note{position:absolute;font-size:3.5px;line-height:4.6px;font-weight:300;color:var(--muted)}
.venue-photo{position:absolute;background:linear-gradient(135deg,#3B4B5E,#8C6B4A)}

/* partners */
.partners{font-size:4.2px;line-height:6.4px;font-weight:700;text-align:center;color:var(--ink)}

/* advertisers */
.logo-grid{position:absolute;left:44px;top:58px;display:grid;grid-template-columns:repeat(4,44px);column-gap:21px;row-gap:6px}
.logo-card{height:19px;background:var(--paper);border-radius:2px;box-shadow:0 0.5px 1.5px rgba(0,0,0,.12);display:flex;align-items:center;justify-content:center;font-size:5px;font-weight:700;color:var(--ink);text-align:center;line-height:5.5px}

/* takeaways & specs */
.checks{list-style:none}
.checks li{position:relative;padding-left:9px;margin-bottom:5px;font-size:3.6px;line-height:4.6px;font-weight:300;color:var(--muted)}
.checks li::before{content:"";position:absolute;left:1px;top:0.5px;width:1.6px;height:3.2px;border:solid var(--blue);border-width:0 0.8px 0.8px 0;transform:rotate(40deg)}
.spec-head{font-size:5px;font-weight:500;margin-bottom:6px}
.orb{position:absolute;border-radius:50%;background:var(--blue)}
.motto{position:absolute;color:var(--paper);font-weight:300;font-size:10px;line-height:19.5px;text-align:center}

/* thanks */
.thanks{position:absolute;left:24px;top:64px;font-size:28px;font-weight:300}
.thanks b{font-weight:700}
</style>
</head>
<body>
<main class="deck">

  <!-- cover variant: lobby -->
  <section class="slide slide--blue">
    <div class="brand brand--cover"><span class="brand__box"></span>Bimvoro</div>
    <h1 class="cover__title"><b>Indoor DOOH</b><br>Audiences at<br>Scale</h1>
    <div class="cover__btn">BUY ON BIMVORO</div>
    <p class="cover__mail">Info@Bimvoro.com</p>
    <div class="cover__photo photo--lobby" role="img" aria-label="Person looking at an indoor digital screen in a bright lobby"></div>
    <div class="cover__kit">MEDIA KIT 2021</div>
  </section>

  <!-- cover variant: screen wall -->
  <section class="slide slide--blue">
    <div class="brand brand--cover"><span class="brand__box"></span>Bimvoro</div>
    <h1 class="cover__title"><b>Indoor DOOH</b><br>Audiences at<br>Scale</h1>
    <div class="cover__btn">BUY ON BIMVORO</div>
    <p class="cover__mail">Info@Bimvoro.com</p>
    <div class="cover__photo photo--wall" role="img" aria-label="Curved wall of many screens showing varied travel scenes"></div>
    <div class="cover__kit">MEDIA KIT 2021</div>
  </section>

  <!-- cover variant: audience detection -->
  <section class="slide slide--blue">
    <div class="brand brand--cover"><span class="brand__box"></span>Bimvoro</div>
    <h1 class="cover__title"><b>Indoor DOOH</b><br>Audiences at<br>Scale</h1>
    <div class="cover__btn">BUY ON BIMVORO</div>
    <p class="cover__mail">Info@Bimvoro.com</p>
    <div class="cover__photo photo--crowd" role="img" aria-label="Shoppers in a mall with audience age and gender labels over them"></div>
    <div class="cover__kit">MEDIA KIT 2021</div>
  </section>

  <!-- why indoor: row layout -->
  <section class="slide">
    <h2 class="heading">WHY GO <b>INDOOR |</b></h2>
    <p class="lede">it's not just lockdowns ending - recent uptick has been driven by the unique effectiveness of indoor DOOH ad exposure.</p>
    <div class="panel" style="left:15px;top:59px;width:167px;height:100px"></div>
    <div class="cols" style="left:20px;top:65px;width:160px;height:90px">
      <div class="col">
        <p class="col__head">It's special...</p>
        <div class="item"><span class="icon"><svg viewBox="0 0 10 10"><ellipse cx="5" cy="5" rx="4" ry="2.4" fill="none" stroke="#fff" stroke-width="1"/><circle cx="5" cy="5" r="1.1" fill="#fff"/></svg></span>Dwell time measured in minutes, not seconds</div>
        <div class="item"><span class="icon"><svg viewBox="0 0 10 10"><circle cx="5" cy="5" r="3.5" fill="none" stroke="#fff" stroke-width="1"/></svg></span>Brand-safe</div>
        <div class="item"><span class="icon"><svg viewBox="0 0 10 10"><circle cx="5" cy="3.5" r="1.6" fill="#fff"/><path d="M2 9a3 3 0 0 1 6 0" fill="#fff"/></svg></span>100% viewability by humans, not bots</div>
        <div class="item"><span class="icon"><svg viewBox="0 0 10 10"><rect x="2" y="2" width="6" height="6" rx="1" fill="none" stroke="#fff" stroke-width="1"/><path d="M4 4l2.5 1-2.5 1z" fill="#fff"/></svg></span>Not Skippable</div>
      </div>
      <div class="col">
        <p class="col__head">It's powerful...</p>
        <div class="item"><span class="icon"><svg viewBox="0 0 10 10"><path d="M2 4h2l4-2v6L4 6H2z" fill="#fff"/></svg></span>Engaged impressions, consumer attention, means...</div>
        <div class="item"><span class="icon"><svg viewBox="0 0 10 10"><circle cx="5" cy="5" r="3.5" fill="none" stroke="#fff" stroke-width="1"/><circle cx="5" cy="5" r="1.3" fill="#fff"/></svg></span>...Indoor DOOH 2x more likely to be seen, recalled, than traditional OOH¹</div>
      </div>
      <div class="col">
        <p class="col__head">And it works.</p>
        <div class="item"><span class="icon"><svg viewBox="0 0 10 10"><path d="M7.8 4A3 3 0 1 0 8 6" fill="none" stroke="#fff" stroke-width="1"/><path d="M8.6 2.4v2.4H6.2z" fill="#fff"/></svg></span>2x increase in reach if added to Omni -Channel campaigns²</div>
      </div>
    </div>
    <p class="notes">1. Source: industry study on omnichannel reach, 2019<br>2. Source: outdoor media research report, 2020</p>
    <div class="cover__photo photo--salon" style="left:200px;width:123px;border-top-left-radius:30px 91px;border-bottom-left-radius:30px 91px" role="img" aria-label="Waiting room with a wall screen showing a service promotion and a customer on her phone"></div>
    <div class="brand brand--foot brand--foot-light"><span class="brand__box"></span>Bimvoro</div>
  </section>

  <!-- why indoor: grid layout -->
  <section class="slide">
    <h2 class="heading" style="top:19px">WHY GO <b>INDOOR |</b></h2>
    <p class="lede">it's not just lockdowns ending - recent uptick has been driven by the unique effectiveness of indoor DOOH ad exposure.</p>
    <div class="panel" style="left:0;top:58px;width:181px;height:105px"></div>
    <div class="cols" style="left:20px;top:62px;width:160px;height:100px">
      <div class="col" style="flex:1.4">
        <p class="col__head">It's special...</p>
        <div style="display:grid;grid-template-columns:1fr 1fr;gap:3px">
          <div class="item item--stack"><span class="icon"><svg viewBox="0 0 10 10"><ellipse cx="5" cy="5" rx="4" ry="2.4" fill="none" stroke="#fff" stroke-width="1"/><circle cx="5" cy="5" r="1.1" fill="#fff"/></svg></span>Dwell time measured in minutes, not seconds</div>
          <div class="item item--stack"><span class="icon"><svg viewBox="0 0 10 10"><circle cx="5" cy="5" r="3.5" fill="none" stroke="#fff" stroke-width="1"/></svg></span>Brand-safe</div>
          <div class="item item--stack"><span class="icon"><svg viewBox="0 0 10 10"><circle cx="5" cy="3.5" r="1.6" fill="#fff"/><path d="M2 9a3 3 0 0 1 6 0" fill="#fff"/></svg></span>100% viewability by humans, not bots</div>
          <div class="item item--stack"><span class="icon"><svg viewBox="0 0 10 10"><rect x="2" y="2" width="6" height="6" rx="1" fill="none" stroke="#fff" stroke-width="1"/><path d="M4 4l2.5 1-2.5 1z" fill="#fff"/></svg></span>Not Skippable</div>
        </div>
      </div>
      <div class="col">
        <p class="col__head">It's powerful...</p>
        <div class="item item--stack"><span class="icon"><svg viewBox="0 0 10 10"><path d="M2 4h2l4-2v6L4 6H2z" fill="#fff"/></svg></span>Engaged impressions, consumer attention, means...</div>
        <div class="item item--stack"><span class="icon"><svg viewBox="0 0 10 10"><circle cx="5" cy="5" r="3.5" fill="none" stroke="#fff" stroke-width="1"/><circle cx="5" cy="5" r="1.3" fill="#fff"/></svg></span>...Indoor DOOH 2x more likely to be seen, recalled, than traditional OOH¹</div>
      </div>
      <div class="col" style="flex:0.8">
        <p class="col__head">And it works.</p>
        <div class="item item--stack"><span class="icon"><svg viewBox="0 0 10 10"><path d="M7.8 4A3 3 0 1 0 8 6" fill="none" stroke="#fff" stroke-width="1"/><path d="M8.6 2.4v2.4H6.2z" fill="#fff"/></svg></span>2x increase in reach if added to Omni -Channel campaigns²</div>
      </div>
    </div>
    <p class="notes" style="bottom:6px">1. Source: industry study on omnichannel reach, 2019<br>2. Source: outdoor media research report, 2020</p>
    <div class="cover__photo photo--salon" style="left:196px;width:127px;border-top-left-radius:30px 91px;border-bottom-left-radius:30px 91px" role="img" aria-label="Waiting room with a wall screen showing a service promotion and a customer on her phone"></div>
    <div class="brand brand--foot brand--foot-light"><span class="brand__box"></span>Bimvoro</div>
  </section>

  <!-- statement -->
  <section class="slide slide--blue">
    <p class="statement">Bimvoro offers advertisers easy, affordable access to <b>North America's largest indoor DOOH network,</b> containing <b>diverse audience segments</b> while <b>captivated in indoor environments</b></p>
    <div class="underline" style="top:123px;width:56px"></div>
  </section>

  <!-- network -->
  <section class="slide">
    <h2 class="heading"><b>NETWORK |</b></h2>
    <p class="lede" style="width:170px">Bimvoro is your DOOH partner, connecting your partners and advertisers to a nation-wide network of premium, place-based screens.</p>
    <div class="panel" style="left:24px;top:70px;width:270px;height:93px"></div>
    <div class="bar" style="left:24px;top:60px;width:134px">Our nationwide network.</div>
    <div class="bar" style="left:164px;top:60px;width:135px">Our premium venue types.</div>
    <div class="map" style="left:32px;top:73px;width:75px;height:38px" role="img" aria-label="Map of the United States with screen locations marked"></div>
    <div class="map" style="left:32px;top:116px;width:64px;height:37px" role="img" aria-label="Map of Canada with screen locations marked"></div>
    <div class="stat" style="right:173px;top:80px">12B+<small>Impressions<br>Annually</small></div>
    <div class="stat" style="right:173px;top:98px">50+<small>DMA's</small></div>
    <div class="stat" style="right:173px;top:116px">26,105+<small>Venues</small></div>
    <div class="stat" style="right:173px;top:135px">31,594+<small>Screens</small></div>
    <div class="stat stat--left" style="left:174px;top:76px;font-size:6.5px;line-height:6.5px">12000+<small>Retail screens</small></div>
    <div class="stat stat--left" style="left:174px;top:92px;font-size:6.5px;line-height:6.5px">16000+<small>Restobar screens</small></div>
    <div class="stat stat--left" style="left:174px;top:110px;font-size:6.5px;line-height:6.5px">2000+<small>Medical screens</small></div>
    <div class="stat stat--left" style="left:174px;top:126px;font-size:6.5px;line-height:6.5px">4000+<small>Grocery screens</small></div>
    <p class="venue-note" style="left:174px;top:143px;width:45px">Plus private airports, hockey arenas, records stores, and many more.</p>
    <div class="venue-photo" style="left:224px;top:72px;width:67px;height:88px" role="img" aria-label="Collage of screens installed in stores, restaurants and clinics"></div>
    <div class="brand brand--foot"><span class="brand__box"></span>Bimvoro</div>
  </section>

  <!-- how to buy -->
  <section class="slide">
    <h2 class="heading">HOW TO <b>BUY |</b></h2>
    <p class="lede" style="width:150px">Bimvoro's network and unique audiences are accessible however you buy your media.</p>
    <div class="panel" style="left:0;top:58px;width:174px;height:104px"></div>
    <div class="cols" style="left:20px;top:64px;width:152px;height:96px">
      <div class="col" style="flex:1.2">
        <p class="col__head">Audiences...</p>
        <div style="display:grid;grid-template-columns:1fr 1fr;gap:3px">
          <div class="item item--stack"><span class="icon"><svg viewBox="0 0 10 10"><circle cx="5" cy="3.5" r="1.6" fill="#fff"/><path d="M2 9a3 3 0 0 1 6 0" fill="#fff"/></svg></span>High net worth</div>
          <div class="item item--stack"><span class="icon"><svg viewBox="0 0 10 10"><rect x="1.8" y="2.5" width="6.4" height="5" fill="none" stroke="#fff" stroke-width="0.9"/><path d="M5 2.5v5" stroke="#fff" stroke-width="0.9"/></svg></span>Sports Fans</div>
          <div class="item item--stack"><span class="icon"><svg viewBox="0 0 10 10"><circle cx="5" cy="5" r="3.5" fill="none" stroke="#fff" stroke-width="1"/><path d="M5 3v2.2l1.5 1" stroke="#fff" stroke-width="0.9" fill="none"/></svg></span>High dwell time</div>
          <div class="item item--stack"><span style="width:14px;height:14px;border:0.5px solid var(--blue);display:block"></span>And many more</div>
        </div>
      </div>
      <div class="col">
        <p class="col__head">...you can buy anywhere...</p>
        <p class="partners">Bidmetric<br>AdDesk Pro<br>Locato<br>Moovia<br>Atrix<br>Fieldsite<br>Combstack<br>Pulsegrid<br>Omnidex · Skyline Media</p>
      </div>
      <div class="col" style="flex:0.9">
        <p class="col__head">...however you'd like.</p>
        <div class="item item--stack"><span class="icon"><svg viewBox="0 0 10 10"><path d="M5 1.5l3 5H2z" fill="#fff"/></svg></span>Direct Buying</div>
        <div class="item item--stack"><span class="icon"><svg viewBox="0 0 10 10"><circle cx="3" cy="3" r="1.2" fill="#fff"/><circle cx="7" cy="3" r="1.2" fill="#fff"/><circle cx="5" cy="7" r="1.2" fill="#fff"/><path d="M3 3l4 0-2 4z" fill="none" stroke="#fff" stroke-width="0.6"/></svg></span>Open RTB</div>
        <div class="item item--stack"><span class="icon"><svg viewBox="0 0 10 10"><rect x="2" y="2" width="6" height="4.5" fill="none" stroke="#fff" stroke-width="0.9"/><path d="M4 8h2" stroke="#fff" stroke-width="0.9"/></svg></span>Programmatic Guaranteed or PMP</div>
      </div>
    </div>
    <div class="cover__photo photo--street" style="left:188px;width:135px;border-top-left-radius:30px 91px;border-bottom-left-radius:30px 91px" role="img" aria-label="Commuters walking across a busy concourse seen from above"></div>
    <div class="brand brand--foot brand--foot-light"><span class="brand__box"></span>Bimvoro</div>
  </section>

  <!-- advertisers -->
  <section class="slide">
    <h2 class="heading"><b>ADVERTISERS |</b></h2>
    <p class="lede">Brands that buy on our network.</p>
    <div class="panel" style="left:0;top:52px;width:323px;height:107px"></div>
    <div class="logo-grid">
      <div class="logo-card">Norbank</div>
      <div class="logo-card">Maison Lair</div>
      <div class="logo-card">Starwell</div>
      <div class="logo-card">Dashly</div>
      <div class="logo-card">Kestrel Motors</div>
      <div class="logo-card">Northland</div>
      <div class="logo-card">Hemlund</div>
      <div class="logo-card">Choco Dots</div>
      <div class="logo-card">Paycircle</div>
      <div class="logo-card">Burger Row</div>
      <div class="logo-card">Puck League</div>
      <div class="logo-card">Pixelplay</div>
      <div class="logo-card">Verant</div>
      <div class="logo-card">Tunely</div>
      <div class="logo-card">Deli Line</div>
      <div class="logo-card">Fizzwater</div>
    </div>
    <div class="brand brand--foot"><span class="brand__box"></span>Bimvoro</div>
  </section>

  <!-- takeaways -->
  <section class="slide">
    <h2 class="heading"><b>BIMVORO |</b></h2>
    <p class="lede">Key Takeaways</p>
    <div class="panel" style="left:0;top:52px;width:323px;height:103px"></div>
    <div class="abs" style="left:25px;top:60px;width:150px">
      <p class="spec-head">Bimvoro is:</p>
      <ul class="checks">
        <li>North America's largest and fastest-growing indoor DOOH screen network</li>
        <li>Powerful enough to capture the attention of nationwide audiences at scale, specific enough to provide access to diverse audience segments</li>
        <li>Programmatically-accessible, ensuring cost-efficiency, transparency and real-time optimizations</li>
        <li>Flexible enough to get any DOOH campaign or integration up and running quickly and without issue</li>
      </ul>
    </div>
    <div class="orb" style="left:179px;top:65px;width:152px;height:152px"></div>
    <p class="motto" style="left:196px;top:100px;width:130px">The Right Time.<br>The Right Message.<br>The Right Audience.</p>
    <div class="brand brand--foot brand--foot-light"><span class="brand__box"></span>Bimvoro</div>
  </section>

  <!-- formats -->
  <section class="slide">
    <h2 class="heading"><b>DIGITAL</b> MEDIA FORMATS |</h2>
    <p class="lede">Specifications</p>
    <div class="panel" style="left:0;top:52px;width:323px;height:103px"></div>
    <div class="abs" style="left:24px;top:58px;width:52px">
      <p class="spec-head">Network</p>
      <ul class="checks"><li>Indoor, 32"-73" Screens</li><li>Full Screen Take Over</li><li>Sold programmatically</li><li>No Blacklisted Advertisers</li><li>Approval Upon Venue Review</li></ul>
    </div>
    <div class="abs" style="left:82px;top:58px;width:62px;border-left:0.5px solid var(--rule);padding-left:4px;height:94px">
      <p class="spec-head">Content Specifications</p>
      <ul class="checks"><li>1920 pixels (w) x 1080 pixels (h) 16:9</li><li>1080 pixels (w) x 1920 pixels (h) 9:16</li><li>Static: PNG, RGB, encoded .JPG or H.264</li><li>Video: .MP3 / encoded .MOV</li><li>Will repurpose TV spots, banner ads, transcode ill-fitting static creatives</li></ul>
    </div>
    <div class="abs" style="left:143px;top:58px;width:80px;border-left:0.5px solid var(--rule);padding-left:4px;height:94px">
      <p class="spec-head">Ad Content Play Suggestions</p>
      <ul class="checks"><li>15 second</li><li>30 second</li><li>60 second</li></ul>
    </div>
    <div class="orb" style="left:186px;top:68px;width:150px;height:150px"></div>
    <p class="motto" style="left:201px;top:103px;width:130px">The Right Time.<br>The Right Message.<br>The Right Audience.</p>
    <div class="brand brand--foot brand--foot-light"><span class="brand__box"></span>Bimvoro</div>
  </section>

  <!-- thank you -->
  <section class="slide slide--blue">
    <p class="thanks">Thank <b>you.</b></p>
    <div class="underline" style="top:111px;width:83px"></div>
  </section>

</main>
</body>
</html>
```